Hotel Lobby sign up to invest banner 4ft by 8 ft

We need to have a 4ft x 8ft banner designed. the sign is to attract investors to purchase condos at The Lodge at Marlowe's Bend. Banner will hang in lobby and an ipad will be available for guest to sign up to get information and investor information.
The wording used should be something similar to or:

You Love the Resort, why not own it?

Sign-Up Here to receive updates & new condo information

Target Market(s)

Condo guest looking to invest

Industry/Entity Type

Hospitality

Requirements
Must have
• Logo and be 4ft by 8 ft
Nice to have
• use the attached map but does not have to
• font has to be eligible
Should not have
• scripted font

```html
<!DOCTYPE html>
<html lang="en">
<head>
<meta charset="utf-8">
<title>The Lodge at Marlowe's Bend – Condo Sign-Up Banner</title>
<link href="https://fonts.googleapis.com/css2?family=Varela+Round&display=swap" rel="stylesheet">
<style>
  :root {
    --stage: #a8dcd8;
    --paper: #f4f4f3;
    --slate-teal: #668c95;
    --headline-teal: #6b8f98;
    --sand: #e0a96b;
    --dusk-blue: #3d4fa8;
    --lamp-gold: #d9a440;
  }
  html, body {
    margin: 0;
    width: 1200px;
    height: 720px;
    overflow: hidden;
    background: var(--stage);
  }
  .banner {
    position: absolute;
    left: 40px;
    top: 128px;
    width: 1120px;
    height: 465px;
    background: var(--paper);
    overflow: hidden;
    font-family: "Varela Round", "Arial Rounded MT Bold", sans-serif;
    box-shadow: 0 6px 18px rgba(40, 90, 90, 0.18);
  }
  .banner-shapes {
    position: absolute;
    inset: 0;
  }
  .brand {
    position: absolute;
    left: 131px;
    top: 58px;
    width: 220px;
    display: flex;
    align-items: center;
    gap: 10px;
    color: var(--headline-teal);
    font-size: 24px;
    line-height: 1.15;
  }
  .brand-mark {
    flex: none;
    width: 14px;
    height: 14px;
    background: var(--sand);
  }
  .headline {
    position: absolute;
    left: 25px;
    top: 196px;
    margin: 0;
    color: var(--headline-teal);
    font-size: 38px;
    font-weight: 400;
    line-height: 52px;
    letter-spacing: 0.2px;
  }
  .signup {
    position: absolute;
    left: 16px;
    top: 310px;
    margin: 0;
    color: var(--sand);
    font-size: 27px;
    line-height: 45px;
  }
  .signup-pill {
    display: inline-block;
    padding: 0 8px;
    background: var(--slate-teal);
    color: var(--sand);
    border-radius: 8px;
    line-height: 41px;
  }
  .signup-detail {
    display: block;
    padding-left: 8px;
    font-size: 25px;
  }
</style>
</head>
<body>
  <section class="banner">
    <svg class="banner-shapes" width="1120" height="465" viewBox="0 0 1120 465">
      <defs>
        <linearGradient id="resort-photo-tones" x1="0" y1="0" x2="1" y2="1">
          <stop offset="0" stop-color="var(--dusk-blue)"/>
          <stop offset="0.45" stop-color="#5a6fb8"/>
          <stop offset="0.7" stop-color="var(--lamp-gold)"/>
          <stop offset="1" stop-color="#5e7a52"/>
        </linearGradient>
      </defs>
      <polygon class="sand-accent" points="429,274 468,274 386,465 339,465" fill="var(--sand)"/>
      <polygon class="teal-band" points="590,0 1120,0 1120,465 386,465" fill="var(--slate-teal)"/>
      <polygon class="sand-frame" points="776,47 1120,47 1120,465 595,465" fill="var(--sand)" opacity="0.85"/>
      <polygon class="resort-photo" points="876,65 1120,65 1120,465 695,465"
               fill="url(#resort-photo-tones)" role="img"
               aria-label="Evening photo of the lodge building with lit balconies, pool deck and water slides"/>
    </svg>

    <div class="brand">
      <span class="brand-mark"></span>
      <span class="brand-name">The Lodge at Marlowe's Bend</span>
    </div>

    <h1 class="headline">You Love the Resort,<br>why not own it?</h1>

    <p class="signup">
      <span class="signup-pill">Sign-Up</span> Here
      <span class="signup-detail">to receive updates &amp;</span>
      <span class="signup-detail">new condo information</span>
    </p>
  </section>
</body>
</html>
```